Marvelin Group business card redesign

Please throw away what we have and start from scratch. We are bored with our Marvelin Group cards, they need a refresh and as we have introduced a new company to the fold it is the perfect time. Please come up with something that pops. Finishes like foil embossing or engraving are all on the table. Please not be afraid to turn it on it's head. Creative people only.
Target Market(s)
From engineers, to builders, to DIY
Industry/Entity Type
Manufacturer
Contact Information for Business Card
Double sided
Colors
9bcb3c
0255a3
0592cd
Requirements
Must have
- All logos must be shown, the four company logs can be on the back. The group logo is the only one that must be on the front. .
Nice to have
- a design that will age well, we are looking for at least 5 years from the cards.
Should not have
- Please do not send me designs which are just templates that are on the internet, you will be wasting your and my time. As I have searched and searched online and have not found anything I like.

```html
<!DOCTYPE html>
<html lang="en">
<head>
<meta charset="utf-8">
<title>Marvelin Group business cards</title>
<link href="https://fonts.googleapis.com/css2?family=Open+Sans:wght@400;600;700;800&display=swap" rel="stylesheet">
<style>
  :root {
    --green: #9bcb3c;
    --blue: #0255a3;
    --navy: #1f3b8f;
    --sky: #0592cd;
    --charcoal: #2b2b2b;
    --ink: #1d1d1d;
    --paper: #ffffff;
    --backdrop: #e9e7e3;
  }
  * { margin: 0; padding: 0; box-sizing: border-box; }
  html, body { width: 1200px; height: 899px; overflow: hidden; }
  body {
    background: var(--backdrop);
    font-family: "Open Sans", Arial, sans-serif;
    display: flex;
    align-items: center;
    justify-content: center;
    gap: 40px;
  }
  .card {
    position: relative;
    width: 540px;
    height: 309px;
    overflow: hidden;
    box-shadow: 0 6px 18px rgba(0,0,0,.18);
  }
  /* Front */
  .card-front { background: var(--paper); }
  .card-front .bands { position: absolute; inset: 0; }
  .corner-mark { position: absolute; left: 22px; top: 22px; width: 30px; height: 30px; }
  .holder { position: absolute; left: 62px; top: 21px; }
  .holder-name { color: var(--navy); font-weight: 700; font-size: 19px; line-height: 1.15; }
  .holder-role { color: var(--ink); font-size: 12px; }
  .address { position: absolute; left: 46px; top: 98px; color: var(--ink); font-size: 13px; line-height: 1.35; }
  .contacts { position: absolute; left: 30px; top: 140px; list-style: none; font-size: 13px; color: var(--ink); line-height: 1.6; }
  .contacts li { display: flex; align-items: center; gap: 7px; }
  .contacts svg { width: 10px; height: 10px; flex: none; }
  .group-name { position: absolute; right: 34px; top: 112px; text-align: right; color: var(--navy); }
  .group-name .word { font-weight: 800; font-size: 44px; letter-spacing: 1px; line-height: 1; }
  .group-name .sub { font-weight: 800; font-size: 14px; letter-spacing: 9px; margin-top: 2px; }

  /* Back */
  .card-back { background: var(--charcoal); }
  .card-back .group-name { right: 50%; transform: translateX(50%); top: 58px; text-align: center; color: var(--paper); }
  .partner-strip {
    position: absolute; left: 0; right: 0; top: 182px; height: 80px;
    background: var(--paper);
    display: flex; align-items: center; justify-content: space-around; padding: 0 14px;
  }
  .partner { display: flex; align-items: center; gap: 6px; color: var(--blue); font-weight: 700; font-size: 13px; }
  .partner .dot { width: 12px; height: 12px; border-radius: 50%; background: var(--green); }
  .partner .dot.sky { background: var(--sky); }
  .partner .dot.square { border-radius: 0; background: var(--blue); }
</style>
</head>
<body>

  <section class="card card-front" aria-label="Business card front">
    <svg class="bands" viewBox="0 0 540 309" aria-hidden="true">
      <polygon points="0,226 220,262 200,282 0,248" fill="var(--green)"/>
      <polygon points="220,262 540,288 540,309 190,309 200,282" fill="var(--navy)"/>
    </svg>
    <svg class="corner-mark" viewBox="0 0 30 30" aria-hidden="true">
      <rect width="30" height="30" fill="var(--navy)"/>
      <polygon points="0,0 30,0 0,30" fill="var(--green)"/>
    </svg>
    <div class="holder">
      <div class="holder-name">Daniel Reeve</div>
      <div class="holder-role">Managing Director</div>
    </div>
    <div class="address">48 Quarry Lane<br>Harbourton, 40217</div>
    <ul class="contacts">
      <li><svg viewBox="0 0 10 10" aria-hidden="true"><path fill="var(--navy)" d="M2 0h2l1 3-1.5 1a6 6 0 0 0 2.5 2.5L7 5l3 1v2c0 1-1 2-2 2A8 8 0 0 1 0 2c0-1 1-2 2-2z"/></svg>(061)-352-4418</li>
      <li><svg viewBox="0 0 10 10" aria-hidden="true"><rect x="1" y="1" width="8" height="8" rx="1" fill="var(--navy)"/></svg>352-901-2276</li>
      <li><svg viewBox="0 0 10 10" aria-hidden="true"><rect x="0" y="2" width="10" height="6.5" fill="var(--navy)"/><path d="M0.5 2.5l4.5 3.2 4.5-3.2" fill="none" stroke="#fff" stroke-width=".9"/></svg>hello@marvelingroup.com</li>
    </ul>
    <div class="group-name">
      <div class="word">MARVELIN</div>
      <div class="sub">GROUP</div>
    </div>
  </section>

  <section class="card card-back" aria-label="Business card back">
    <div class="group-name">
      <div class="word">MARVELIN</div>
      <div class="sub">GROUP</div>
    </div>
    <div class="partner-strip">
      <div class="partner"><span class="dot"></span>Marvelin</div>
      <div class="partner"><span class="dot square"></span>Kestra Roll Works</div>
      <div class="partner"><span class="dot sky"></span>Norvale Foam</div>
      <div class="partner">Tarro Steel</div>
    </div>
  </section>

</body>
</html>
```